Verdant Orthodontics needs bag design to promote "Grin Voyage"

This SMALL 20cm by 20cm (8 in by 8 in) white canvas bag will be given out to all patients who start their orthodontic treatment with us. Our logo and the bag image are attached. Want to include some sort of our logo/name, and 'established 2011' and 'SMILE MORE, BE HAPPIER' or some other fun/cute sentence. Want this bag to be cute/fun/fashionable.

Target Market(s)

moms, adolescent kids

Industry/Entity Type

dentistry, orthodontics

Colors
0094D4
00A9DD
6FCCEA
C7EBF8
E9F6FB

Requirements
Must have
• (modified )logo/name, simplicity

```html
<!DOCTYPE html>
<html lang="en">
<head>
<meta charset="utf-8">
<title>Verdant Orthodontics – Smile more, be happier</title>
<link rel="stylesheet" href="https://fonts.googleapis.com/css2?family=Montserrat:wght@500;700&family=Mulish:wght@300;400&family=Allura&family=Sacramento&display=swap">
<style>
  :root {
    --white: #ffffff;
    --sky-deep: #6fcce0;
    --sky-soft: #c7ebf8;
    --sky-mist: #e9f6fb;
    --stone: #8c8789;
    --stone-light: #a9a5a7;
  }
  * { margin: 0; padding: 0; box-sizing: border-box; }
  html, body {
    width: 1200px;
    height: 1200px;
    overflow: hidden;
    background: var(--white);
  }
  .bag-print {
    position: relative;
    width: 1200px;
    height: 1200px;
    background: var(--white);
  }
  .established {
    position: absolute;
    top: 72px;
    left: 0;
    width: 100%;
    text-align: center;
    font-family: "Montserrat", sans-serif;
    font-weight: 500;
    font-size: 27px;
    letter-spacing: 0.42em;
    color: var(--stone);
  }
  .established .year {
    font-weight: 700;
    color: var(--sky-deep);
  }
  .tooth-crowd {
    position: absolute;
    left: 120px;
    top: 145px;
    width: 980px;
    height: 790px;
    border-radius: 46% 46% 40% 40% / 38% 38% 30% 30%;
    background: radial-gradient(ellipse at center, var(--sky-mist) 0%, #f3fafd 70%, var(--white) 100%);
  }
  .slogan-main {
    position: absolute;
    left: 0;
    top: 330px;
    width: 100%;
    text-align: center;
    font-family: "Allura", cursive;
    font-size: 330px;
    line-height: 1;
    color: var(--sky-deep);
  }
  .slogan-sub {
    position: absolute;
    left: 390px;
    top: 565px;
    width: 420px;
    text-align: center;
    font-family: "Sacramento", cursive;
    font-size: 86px;
    line-height: 0.95;
    color: var(--stone);
  }
  .brand-dot {
    position: absolute;
    left: 577px;
    top: 965px;
    width: 46px;
    height: 46px;
    border-radius: 50%;
    background: var(--sky-deep);
  }
  .brand-name {
    position: absolute;
    top: 1030px;
    left: 0;
    width: 100%;
    text-align: center;
    font-family: "Mulish", sans-serif;
    font-weight: 400;
    font-size: 48px;
    letter-spacing: 0.01em;
    color: var(--stone);
  }
  .brand-tagline {
    position: absolute;
    top: 1098px;
    left: 0;
    width: 100%;
    text-align: center;
    font-family: "Mulish", sans-serif;
    font-weight: 300;
    font-size: 26px;
    color: var(--stone-light);
  }
</style>
</head>
<body>
  <main class="bag-print">
    <p class="established">ESTABLISHED <span class="year">2011</span></p>

    <div class="tooth-crowd" role="img" aria-label="Light blue sketched illustration of a cheerful group of cartoon teeth"></div>

    <h1 class="slogan-main">Smile</h1>
    <p class="slogan-sub">more,<br>be happier</p>

    <div class="brand-dot"></div>
    <p class="brand-name">verdant orthodontics</p>
    <p class="brand-tagline">for children and adults</p>
  </main>
</body>
</html>
```